Build me a WordPress Website For Basketball team, I will put all the details soon, just show me some templates or special WordPress designs for that purpose, you must build the website after I choose the winner design, good luck for everybody, if you have a full functional live preview or demo for your design "not just a live large photo" it will be a great advantage for you to win this contest.

```html
<!DOCTYPE html>
<html lang="en">
<head>
<meta charset="utf-8">
<title>Courtside — Basketball Club</title>
<link href="https://fonts.googleapis.com/css2?family=Abel&family=Raleway:ital,wght@0,300;0,400;0,600;0,700;1,700&family=Work+Sans:wght@400;600;700&display=swap" rel="stylesheet">
<style>
:root{
  --admin-bg:#23282d;
  --admin-text:#eeeeee;
  --admin-badge:#ca4a1f;
  --hero-deep:#2a0b30;
  --hero-mid:#4a2150;
  --hero-warm:#6a3a52;
  --title-yellow:#f1e64a;
  --white:#ffffff;
  --rule:rgba(255,255,255,.22);
  --content-bg:#2d0c33;
  --meta:#c9b8cc;
  --chat-blue:#1b7ed8;
  --share-blue:#3b6fc4;
}
*{margin:0;padding:0;box-sizing:border-box}
html,body{width:1200px;height:841px;overflow:hidden;background:var(--content-bg)}
body{position:relative;font-family:'Raleway',sans-serif;color:var(--white)}

.admin-bar{position:absolute;top:0;left:0;width:1200px;height:35px;background:var(--admin-bg);
  font-family:Arial,Helvetica,sans-serif;font-size:13px;color:var(--admin-text);display:flex;align-items:center}
.admin-bar .item{display:flex;align-items:center;gap:6px;margin-left:13px}
.admin-bar .item:first-child{margin-left:12px}
.admin-bar .dot{width:18px;height:18px;border-radius:50%;background:#9aa0a6}
.admin-bar .badge{background:var(--admin-badge);color:#fff;border-radius:9px;font-size:11px;padding:1px 6px}
.admin-bar .right{margin-left:auto;display:flex;align-items:center;gap:8px;margin-right:12px}
.admin-bar .avatar{width:17px;height:17px;background:#c9c9c9;border:2px solid #eee}

.hero{position:absolute;top:35px;left:0;width:1200px;height:662px;
  background:radial-gradient(ellipse at 55% 45%,var(--hero-warm) 0%,var(--hero-mid) 40%,var(--hero-deep) 100%)}
.hero-band{position:absolute;left:0;top:340px;width:1200px;height:322px;
  background:linear-gradient(180deg,rgba(60,30,70,0) 0%,rgba(80,45,85,.55) 50%,rgba(40,15,45,.6) 100%)}

.site-header{position:absolute;top:35px;left:127px;width:953px;height:69px;border-bottom:1px solid var(--rule)}
.brand{position:absolute;left:0;top:22px;display:flex;align-items:center;gap:8px;font-family:'Work Sans',sans-serif;font-size:22px;font-weight:600}
.brand .mark{width:17px;height:17px;border-radius:50%;background:var(--title-yellow)}
.main-nav{position:absolute;left:458px;top:24px;font-family:'Work Sans',sans-serif;font-size:12px;font-weight:700;letter-spacing:.5px}
.search{position:absolute;right:0;top:16px;width:140px;height:34px;border-radius:17px;background:rgba(255,255,255,.08);
  font-size:10px;color:rgba(255,255,255,.35);padding:10px 12px}

.slide-title{position:absolute;top:274px;left:0;width:1200px;text-align:center;font-size:45px;font-weight:300;color:var(--title-yellow);letter-spacing:.3px}
.slide-text{position:absolute;top:365px;left:0;width:1208px;text-align:center;font-size:13px;color:rgba(255,255,255,.75)}
.read-more{position:absolute;top:411px;left:513px;width:179px;height:45px;border:1px solid rgba(255,255,255,.35);
  display:flex;align-items:center;justify-content:center;font-size:13px;font-weight:700;font-style:italic}
.slide-next{position:absolute;top:336px;left:1152px;width:42px;height:42px;border-radius:50%;background:rgba(255,255,255,.18);
  display:flex;align-items:center;justify-content:center}

.breadcrumb-bar{position:absolute;top:613px;left:127px;width:953px;border-top:1px solid var(--rule);
  text-align:center;padding-top:35px;font-size:11px;font-weight:600;letter-spacing:.4px}

.share-box{position:absolute;top:273px;left:13px;width:78px;height:230px;background:var(--white);border-radius:3px;
  box-shadow:0 1px 6px rgba(0,0,0,.3);font-family:Arial,sans-serif}
.share-box .count{position:absolute;top:21px;left:15px;width:48px;height:18px;border:1px solid #bbb;color:#333;font-size:11px;text-align:center;line-height:16px}
.share-box .like{position:absolute;top:39px;left:15px;width:48px;height:16px;background:var(--share-blue);color:#fff;font-size:10px;font-weight:700;text-align:center;line-height:16px}
.share-box .post{position:absolute;top:111px;left:11px;width:56px;height:20px;background:#2b9ae6;color:#fff;font-size:11px;font-weight:700;text-align:center;line-height:20px;border-radius:3px}
.share-box .plus{position:absolute;top:155px;left:15px;width:48px;height:20px;border:1px solid #bbb;color:#c43d2e;font-size:11px;text-align:center;line-height:18px;border-radius:2px}
.share-box .hide{position:absolute;top:210px;left:0;width:78px;text-align:center;color:#aaa;font-size:9px}

.post-header{position:absolute;top:732px;left:125px;width:660px}
.post-title{font-family:'Abel',sans-serif;font-size:36px;font-weight:400;line-height:43px}
.post-meta{margin-top:16px;font-size:11px;color:var(--meta);word-spacing:2px}

.sidebar{position:absolute;top:740px;left:827px;width:253px}
.widget-title{display:flex;align-items:center;gap:12px;font-size:12px;font-weight:600;letter-spacing:.3px}
.widget-title::after{content:"";flex:1;height:1px;background:var(--rule)}
.recent-link{margin-top:34px;font-size:13px;line-height:20px}

.chat-button{position:absolute;top:805px;left:1037px;width:163px;height:36px;background:var(--chat-blue);border-radius:4px 0 0 0;
  display:flex;align-items:center;justify-content:center;gap:7px;font-family:Arial,sans-serif;font-size:16px}
.chat-button .sq{width:16px;height:16px;background:#fff;border-radius:2px}
</style>
</head>
<body>

<div class="admin-bar">
  <div class="item"><span class="dot"></span></div>
  <div class="item">
    <svg width="14" height="14" viewBox="0 0 14 14"><path d="M2 12V5l5-3 5 3v7z" fill="#a0a5aa"/></svg>hoopline.net</div>
  <div class="item">
    <svg width="14" height="14" viewBox="0 0 14 14"><path d="M2 12l8-8 2 2-8 8H2z" fill="#a0a5aa"/></svg>Customize</div>
  <div class="item">
    <svg width="14" height="14" viewBox="0 0 14 14"><circle cx="7" cy="7" r="5" fill="none" stroke="#a0a5aa" stroke-width="2"/></svg>21</div>
  <div class="item">
    <svg width="14" height="14" viewBox="0 0 14 14"><path d="M1 2h12v8H5l-3 3V10H1z" fill="#a0a5aa"/></svg>0</div>
  <div class="item">
    <svg width="12" height="12" viewBox="0 0 12 12"><path d="M5 0h2v5h5v2H7v5H5V7H0V5h5z" fill="#a0a5aa"/></svg>New</div>
  <div class="item"><span class="badge">3</span></div>
  <div class="item">
    <svg width="14" height="14" viewBox="0 0 14 14"><circle cx="7" cy="7" r="4" fill="#a0a5aa"/></svg>Pipewren</div>
  <div class="item">
    <svg width="14" height="14" viewBox="0 0 14 14"><circle cx="7" cy="7" r="5" fill="none" stroke="#a0a5aa" stroke-width="3" stroke-dasharray="3 2"/></svg>Ad Placer</div>
  <div class="right">
    <span>Howdy, Marco Delgado</span><span class="avatar"></span>
    <svg width="16" height="16" viewBox="0 0 16 16"><circle cx="6.5" cy="6.5" r="4.5" fill="none" stroke="#eee" stroke-width="2"/><path d="M10 10l4 4" stroke="#eee" stroke-width="2"/></svg>
  </div>
</div>

<section class="hero" role="img" aria-label="Photo of a basketball player taking a jump shot in an indoor gym, tinted purple">
  <div class="hero-band"></div>
</section>

<header class="site-header">
  <div class="brand"><span class="mark"></span>Courtside</div>
  <nav class="main-nav">HOME</nav>
  <div class="search">Search</div>
</header>

<h1 class="slide-title">THERE LIVE THE BLIND TEXTS</h1>
<p class="slide-text">Far far away, behind the word mountains, far from the countries Vokalia and Consonantia, there live the blind texts</p>
<div class="read-more">READ MORE</div>
<div class="slide-next">
  <svg width="12" height="14" viewBox="0 0 12 14"><path d="M3 1l6 6-6 6" fill="none" stroke="#fff" stroke-width="2.5"/></svg>
</div>

<div class="breadcrumb-bar">HOME</div>

<aside class="share-box">
  <div class="count">130</div>
  <div class="like">Like</div>
  <div class="post">Post</div>
  <div class="plus">Share</div>
  <div class="hide">Hide</div>
</aside>

<article class="post-header">
  <h2 class="post-title">Application Form Is Defective: Valderama Amnesty Case</h2>
  <p class="post-meta">November 6, 2018 &nbsp; / &nbsp; Politics &nbsp; / &nbsp; No comments &nbsp; / &nbsp; | Edit &nbsp; / &nbsp; Marco Delgado</p>
</article>

<aside class="sidebar">
  <div class="widget-title">RECENT POST</div>
  <p class="recent-link">Application Form Is Defective: Valderama Amnesty Case</p>
</aside>

<div class="chat-button"><span class="sq"></span>Chat us Live!</div>

</body>
</html>
```